Design a calming beauty medical salon & spa website based in Hong Kong

We need help building an informational website for a beauty salon in Hong Kong. The local salon provides facials, massages, body and other slimming treatments in a relaxing environment. We offer some non-invasive medical treatments, such as botox. Having built the business on word of mouth, it is now time for us to launch a website to help market the business better. Website requirements:

-Must be responsive
-Use vibrant but clean colours. not too many, 1-2 colours
-Must be bilingual (switch between Chinese traditional and English)
-Our current website is host on a server, not using any particular platforms like wordpress

Pages:
1/ Homepage
2/ About us (incorporate gallery of salon photos and history of company)
3/ Promotions and latest deals (and leads them to sign up for more info, maybe pop-up small window when you click on a promotion)
4/ Treatment menus
4.1/Body treatments
4.2/ Face treatments
4.3/ Slimming treatments
5/ Showcasing products sold (no e-commerce functionality, just showing off products)
6/ Contact us (tel, address, map, opening hrs)

Footer - must haves include contact us info, privacy policy, terms & conditions, copyright blurb, join our company/employment page (with a form)

For information (comparable websites we like):
http://velarine.com/
http://mottaqua.com.hk/tc/aboutmottaqua/background.php#centerenvi
Attaching a very first draft concept for this website
Attaching pictures of the beauty salon
Attaching logo

Target Market(s)

Hong Kong based, Chinese, females, 30-50+ age. 90% female clients.

Industry/Entity Type

Beauty Salon

Number of Pages Required

5+ page

Font styles to use
Sans Serif

Colors
f9d9e8
fbd3d4
fee3d5
fbe7d2
fee18a
fbf289
ffffff

Requirements
Must have
• interactive elements on website, such as scrolling banner photo headers
• incorporate photos of website salon
• connect to facebook page

```html
<!DOCTYPE html>
<html lang="en">
<head>
<meta charset="utf-8">
<title>Serene Glow – Beauty Salon &amp; Spa</title>
<link href="https://fonts.googleapis.com/css2?family=Quicksand:wght@400;500;600&display=swap" rel="stylesheet">
<style>
:root{
  --rose:#e49a93;
  --rose-deep:#d98a84;
  --rose-band:#e3a59e;
  --blush:#fbd3d4;
  --peach:#fee3d5;
  --cream:#fbeee6;
  --nav:#fbe7d2;
  --plum:#7a2f7c;
  --text:#4a4a4a;
  --muted:#8a8a8a;
  --footer:#3f3f41;
  --footer-deep:#2f2f31;
  --white:#ffffff;
}
*{box-sizing:border-box;margin:0;padding:0}
html,body{width:1200px;height:2912px;overflow:hidden}
body{font-family:"Quicksand",sans-serif;color:var(--text);background:var(--white);position:relative}
a{color:inherit;text-decoration:none}

/* header */
.site-header{position:absolute;top:0;left:0;width:1200px;height:112px;background:var(--white)}
.brand{position:absolute;left:80px;top:34px;display:flex;align-items:center;gap:12px;font-size:30px;font-weight:600;color:var(--plum)}
.brand-dot{width:28px;height:28px;border-radius:50%;background:var(--plum)}
.header-contact{position:absolute;left:470px;top:64px;display:flex;gap:60px;font-size:14px;color:var(--muted)}
.header-contact span{display:flex;align-items:center;gap:8px}
.header-tools{position:absolute;right:80px;top:20px;display:flex;gap:18px;align-items:center}
.lang-flag{width:28px;height:18px;background:#d8342b}

.main-nav{position:absolute;top:112px;left:0;width:1200px;height:56px;background:var(--nav);display:flex;justify-content:space-around;align-items:center;padding:0 60px;font-size:16px;font-weight:500}

/* hero */
.hero{position:absolute;top:168px;left:0;width:1200px;height:652px;background:linear-gradient(100deg,#f4cdc8 0%,#f7d6d1 40%,#f5d0ca 100%);overflow:hidden}
.hero-photo{position:absolute;left:160px;top:0;width:1040px;height:652px;
  background:
    radial-gradient(ellipse 180px 230px at 62% 38%,#eab9a4 0%,#efc7b5 55%,rgba(239,199,181,0) 100%),
    radial-gradient(ellipse 260px 300px at 72% 28%,#6b3f2e 0%,#8c5a45 45%,rgba(140,90,69,0) 100%),
    radial-gradient(ellipse 300px 200px at 70% 95%,#efc4b2 0%,rgba(239,196,178,0) 100%),
    radial-gradient(ellipse 330px 70px at 32% 80%,#f0c3b2 0%,rgba(240,195,178,0) 100%)}
.hero-circle{position:absolute;left:120px;top:70px;width:360px;height:360px;border-radius:50%;background:rgba(255,255,255,.25);display:flex;flex-direction:column;justify-content:center;align-items:center;color:var(--white);font-size:54px;line-height:1.25;text-align:center}

/* services intro */
.intro{position:absolute;top:820px;left:0;width:1200px;height:660px;background:var(--white)}
.intro-photo-a{position:absolute;left:88px;top:112px;width:240px;height:300px;border:8px solid var(--white);box-shadow:0 2px 10px rgba(0,0,0,.14);
  background:radial-gradient(ellipse 70px 90px at 50% 42%,#eec6ad 0%,rgba(238,198,173,0) 100%),radial-gradient(ellipse 110px 150px at 50% 40%,#3a2620 0%,rgba(58,38,32,0) 100%),linear-gradient(180deg,#f3f0ee,#e6dcd6)}
.intro-photo-b{position:absolute;left:268px;top:250px;width:340px;height:330px;border:8px solid var(--white);box-shadow:0 2px 10px rgba(0,0,0,.16);
  background:radial-gradient(ellipse 150px 60px at 50% 88%,#f2e6c8 0%,rgba(242,230,200,0) 100%),radial-gradient(ellipse 160px 180px at 55% 45%,#c98a67 0%,rgba(201,138,103,0) 100%),linear-gradient(150deg,#5c3a2c,#8d5a42 55%,#b07858)}
.intro-text{position:absolute;left:680px;top:152px;width:440px}
.intro-text h2{font-size:46px;font-weight:400;line-height:1.25}
.intro-text h2 em{font-style:normal;color:var(--rose)}
.intro-text p{margin-top:24px;font-size:13px;line-height:1.75;color:var(--muted)}
.btn-outline{display:inline-block;margin-top:28px;padding:12px 28px;border:1px solid var(--rose);border-radius:24px;font-size:15px}

/* treatments */
.treatments{position:absolute;top:1480px;left:0;width:1200px;height:300px;background:linear-gradient(180deg,var(--white) 0,var(--white) 110px,var(--rose-band) 110px,var(--rose-deep) 300px)}
.treatment{position:absolute;top:0;width:300px;text-align:center;color:var(--white)}
.treatment .icon{width:150px;height:150px;margin:0 auto;border-radius:50%;background:var(--peach);display:flex;align-items:center;justify-content:center}
.treatment h3{margin-top:24px;font-size:27px;font-weight:400}
.treatment a{display:block;margin-top:8px;font-size:13px}

/* products */
.products{position:absolute;top:1780px;left:0;width:1200px;height:720px;background:var(--cream)}
.products h2{position:absolute;top:92px;width:1200px;text-align:center;font-size:50px;font-weight:400}
.products .rule{position:absolute;top:184px;left:430px;width:340px;height:1px;background:#d8c4b8}
.product{position:absolute;top:260px;width:240px}
.product .thumb{height:152px}
.product p{margin-top:44px;font-size:14px;line-height:1.55}
.price{margin-top:16px;font-size:13px;display:flex;gap:26px}
.price s{color:var(--muted)}
.price b{font-weight:500;color:var(--rose)}
.btn-fill{display:block;width:120px;margin:30px auto 0;padding:9px 0;border-radius:20px;background:#ecb4aa;color:var(--white);font-size:13px;text-align:center}

/* footer */
.site-footer{position:absolute;top:2500px;left:0;width:1200px;height:380px;background:var(--footer);color:#cfcfcf;font-size:14px}
.site-footer h4{font-size:20px;font-weight:500;color:#e0bdb3;letter-spacing:1px}
.foot-col{position:absolute;top:72px}
.foot-col p{margin-top:16px;line-height:1.6;display:flex;gap:10px}
.links{display:grid;grid-template-columns:110px 110px;gap:14px 10px;margin-top:22px}
.pages li{list-style:none;margin-top:20px}
.form-field{width:240px;height:38px;margin-top:14px;background:var(--white);padding:0 12px;font-size:13px;color:var(--muted);display:flex;align-items:center}
.form-submit{width:240px;height:34px;margin-top:14px;background:var(--peach);color:var(--text);font-size:13px;font-weight:600;display:flex;align-items:center;justify-content:center}
.copyright{position:absolute;top:2880px;left:0;width:1200px;height:32px;background:var(--footer-deep);color:#9a9a9a;font-size:12px;text-align:center;line-height:32px}
</style>
</head>
<body>

<header class="site-header">
  <div class="brand"><span class="brand-dot"></span>Serene Glow</div>
  <div class="header-contact">
    <span><svg width="14" height="11" viewBox="0 0 14 11"><rect x=".5" y=".5" width="13" height="10" fill="none" stroke="#e49a93"/><path d="M.5 .5 7 6 13.5 .5" fill="none" stroke="#e49a93"/></svg>hello@sereneglow.hk</span>
    <span><svg width="12" height="14" viewBox="0 0 12 14"><path d="M2 1h3l1 3-2 1.5a7 7 0 0 0 3.5 3.5L9 7l3 1v3l-1.5 2C5 12.5 0 7.5 1 2z" fill="#e49a93"/></svg>2345 6789 / 6123 4567</span>
  </div>
  <div class="header-tools">
    <svg width="20" height="20" viewBox="0 0 20 20"><circle cx="8" cy="8" r="6" fill="none" stroke="#999" stroke-width="2"/><path d="M12.5 12.5 18 18" stroke="#999" stroke-width="2"/></svg>
    <span class="lang-flag"></span>
  </div>
</header>

<nav class="main-nav">
  <a href="#">Home</a><a href="#">About us</a><a href="#">Promotions and latest deals</a><a href="#">Treatment menus&nbsp;&nbsp;Products</a><a href="#">Contact us</a>
</nav>

<section class="hero">
  <div class="hero-photo" role="img" aria-label="Smiling woman with smooth skin and dark hair holding out an open hand"></div>
  <div class="hero-circle"><span>Relax,</span><span>Renew</span><span>&amp; Pamper</span></div>
</section>

<section class="intro">
  <div class="intro-photo-a" role="img" aria-label="Portrait of a smiling client after a facial"></div>
  <div class="intro-photo-b" role="img" aria-label="Client receiving a relaxing back massage with flowers"></div>
  <div class="intro-text">
    <h2>All for <em>Beauty</em><br>Services</h2>
    <p>Lorem ipsum is simply dummy text of the printing and typesetting industry. Lorem ipsum has been the industry's standard dummy text ever since the 1500s, when an unknown printer took a galley of type and scrambled it to make a type specimen book. It has survived not only five centuries, but also the leap into electronic typesetting, remaining essentially unchanged.</p>
    <a class="btn-outline" href="#">Get an Appointment</a>
  </div>
</section>

<section class="treatments">
  <div class="treatment" style="left:110px">
    <div class="icon"><svg width="70" height="50" viewBox="0 0 70 50"><circle cx="14" cy="16" r="7" fill="#e8a58f"/><path d="M6 32h58v6H6z" fill="#e8a58f"/><path d="M24 26h36l-4 6H22z" fill="#e8a58f"/></svg></div>
    <h3>Body treatments</h3><a href="#">Learn more</a>
  </div>
  <div class="treatment" style="left:450px">
    <div class="icon"><svg width="50" height="60" viewBox="0 0 50 60"><ellipse cx="25" cy="30" rx="16" ry="20" fill="none" stroke="#e8a58f" stroke-width="4"/><path d="M9 22q16-14 32 0" fill="none" stroke="#e8a58f" stroke-width="4"/></svg></div>
    <h3>Face treatments</h3><a href="#">Learn more</a>
  </div>
  <div class="treatment" style="left:790px">
    <div class="icon"><svg width="60" height="66" viewBox="0 0 60 66"><circle cx="30" cy="10" r="7" fill="#e8a58f"/><path d="M8 22h44M30 20v22M30 42l-10 20M30 42l10 20" stroke="#e8a58f" stroke-width="5" fill="none"/></svg></div>
    <h3>Slimming treatments</h3><a href="#">Learn more</a>
  </div>
</section>

<section class="products">
  <h2>Our Featured Products</h2>
  <div class="rule"></div>
  <div class="product" style="left:88px">
    <div class="thumb" role="img" aria-label="Jar of white face cream with flowers" style="background:radial-gradient(ellipse 60px 40px at 45% 60%,#ffffff 0%,rgba(255,255,255,0) 100%),linear-gradient(180deg,#eef2f1,#cfd9d8)"></div>
    <p>Lorem ipsum is simply dummy text of the printing.</p>
    <div class="price"><s>HK$ 980</s><b>HK$ 780</b></div>
    <a class="btn-fill" href="#">Learn more</a>
  </div>
  <div class="product" style="left:354px">
    <div class="thumb" role="img" aria-label="Skin cream dabbed on fingertip" style="background:radial-gradient(ellipse 50px 60px at 50% 55%,#d9a88c 0%,rgba(217,168,140,0) 100%),linear-gradient(180deg,#f4e2d6,#e4c3ae)"></div>
    <p>Lorem ipsum is simply dummy text of the printing.</p>
    <div class="price"><s>HK$ 980</s><b>HK$ 780</b></div>
    <a class="btn-fill" href="#">Learn more</a>
  </div>
  <div class="product" style="left:620px">
    <div class="thumb" role="img" aria-label="Amber serum bottle with dropper" style="background:radial-gradient(ellipse 30px 55px at 45% 60%,#c98a2c 0%,rgba(201,138,44,0) 100%),linear-gradient(180deg,#b8d09a,#7c9a4e)"></div>
    <p>Lorem ipsum is simply dummy text of the printing.</p>
    <div class="price"><s>HK$ 980</s><b>HK$ 780</b></div>
    <a class="btn-fill" href="#">Learn more</a>
  </div>
  <div class="product" style="left:880px">
    <div class="thumb" role="img" aria-label="Row of cosmetic bottles and tubes" style="background:radial-gradient(ellipse 100px 50px at 50% 65%,#ffffff 0%,rgba(255,255,255,0) 100%),linear-gradient(180deg,#eceae6,#cbc5bc)"></div>
    <p>Lorem ipsum is simply dummy text of the printing.</p>
    <div class="price"><s>HK$ 980</s><b>HK$ 780</b></div>
    <a class="btn-fill" href="#">Learn more</a>
  </div>
</section>

<footer class="site-footer">
  <div class="foot-col" style="left:80px;width:260px">
    <h4>LOCATION</h4>
    <p><svg width="12" height="16" viewBox="0 0 12 16"><path d="M6 0a6 6 0 0 1 6 6c0 4-6 10-6 10S0 10 0 6a6 6 0 0 1 6-6z" fill="#e0bdb3"/></svg>12/F, Harbour Light Plaza,<br>88 Lotus Road, Causeway Bay</p>
    <p><svg width="12" height="14" viewBox="0 0 12 14"><path d="M2 1h3l1 3-2 1.5a7 7 0 0 0 3.5 3.5L9 7l3 1v3l-1.5 2C5 12.5 0 7.5 1 2z" fill="#e0bdb3"/></svg>2345 6789</p>
    <p><svg width="14" height="14" viewBox="0 0 14 14"><circle cx="7" cy="7" r="6" fill="none" stroke="#e0bdb3" stroke-width="1.5"/><path d="M7 3v4h3" stroke="#e0bdb3" stroke-width="1.5" fill="none"/></svg>Mon to Fri: 10:30 am to 7:30 pm<br>Sat &amp; holiday: 10:30 am to 5:30 pm</p>
  </div>
  <div class="foot-col" style="left:392px">
    <h4>QUICK LINKS</h4>
    <div class="links"><a>Home</a><a>About us</a><a>Promotions</a><a>Latest deals</a><a>Treatments</a><a>Products</a><a>Contact us</a></div>
  </div>
  <div class="foot-col pages" style="left:648px">
    <h4>PAGES</h4>
    <ul><li>Delivery Information</li><li>Privacy Policy</li><li>Terms &amp; Conditions</li></ul>
  </div>
  <div class="foot-col" style="left:872px">
    <h4>CONTACT US</h4>
    <div class="form-field">Name</div>
    <div class="form-field">Email Id</div>
    <div class="form-field">Phone Number</div>
    <div class="form-submit">SUBMIT</div>
  </div>
</footer>
<div class="copyright">Copyright © 2017 Serene Glow. All rights reserved.</div>

</body>
</html>
```